ATTORNEY FULL PAGE AD

We need a full page flyer for our law firm. We are sending it to people who were in an auto accident and injured. I want to let people know that by hiring an attorney that does not mean that they are suing someone. We will just help them in filing a claim and to get them compensated for: medical bills, lost wages, car repairs, future medical treatment or surgery, and pain/suffering. They will NOT have to pay us any money unless we get them paid. I want to show that we are compassionate to the fact that they went through this tramatic event that will effect their lives for ever. They do not have to worry about anything once they hire us. Our website is: www.brightwelllawfirm.com Our colors are black and gold. NO GAMBLING REFERENCES!!!!
Updates

Don't worry so much about content and wording. Once we get a design and images that look great we will message you the exact words we would like put into the paragraphs. The overall "look" and images are the most important. If anyone has a great change-up logo we are open to it as well. Thanks for everyone's hard work!

We like the dark colors. Some of the images are a little cheesy. We are a family business and treat are clients as family. I like the pictures o the car crashes an the hands. No blood. We want to come off as respectful and trustworthy. It's more about how we will care for them as family than getting them lots of money. 

Target Market(s)

People who were in major accidents and have serious injuries

Industry/Entity Type

Attorney

Requirements
Must have
• Must have our phone number: 1-855-MBRIGHT
Website: www.brightwelllawfirm.com
Company name: Brightwell Law Group
Attorney name: Morgan Ellis Brightwell
High gloss with card stock paper.
Classy - NOT cheesy
Should not have
• No cartoons. Very masculine and professional. There may have been death involved in the accident so we want the ad to be very compassionate and moving.

```html
<!DOCTYPE html>
<html lang="en">
<head>
<meta charset="utf-8">
<title>Brightwell Law Group – Injury Ad</title>
<link rel="stylesheet" href="https://fonts.googleapis.com/css2?family=Cinzel:wght@400;700&family=Yanone+Kaffeesatz:wght@400;500&family=Arimo:wght@400;700&display=swap">
<style>
  :root {
    --black: #000;
    --gold: #f2c14e;
    --gold-deep: #c8922a;
    --amber: #f0b43a;
    --white: #fff;
    --red: #b83a36;
    --red-bright: #d9534a;
    --steel: #3f5670;
    --panel-gray: #5a5a5a;
    --footer-box: #1e1e1e;
  }
  * { margin: 0; padding: 0; box-sizing: border-box; }
  html, body { width: 927px; height: 1200px; overflow: hidden; background: var(--black); }
  .flyer { position: relative; width: 927px; height: 1200px; background: var(--black); overflow: hidden; font-family: "Arimo", Arial, sans-serif; color: var(--white); }
  .backdrop { position: absolute; inset: 0; }
  .crash-photo { position: absolute; left: 0; top: 0; width: 620px; height: 760px;
    background: radial-gradient(ellipse at 45% 45%, #b9bcc0 0%, #8a8d92 22%, #a33a30 38%, #5b4a42 55%, #222 75%, rgba(0,0,0,0) 92%);
    -webkit-mask-image: radial-gradient(ellipse 70% 65% at 45% 45%, #000 55%, transparent 100%);
    mask-image: radial-gradient(ellipse 70% 65% at 45% 45%, #000 55%, transparent 100%); }
  .logo-plate { position: absolute; left: 53px; top: 20px; width: 420px; height: 167px;
    background: linear-gradient(180deg, #6b6b6b, var(--panel-gray) 50%, #3c3c3c);
    display: flex; align-items: center; justify-content: center; }
  .logo-name { font-family: "Cinzel", serif; font-weight: 400; font-size: 34px; color: var(--gold); text-align: center; line-height: 1.2; }
  .attorney-portrait { position: absolute; left: 607px; top: 33px; width: 233px; height: 280px;
    background: linear-gradient(180deg, #4a4038 0%, #2b2622 45%, #15171c 100%); }
  .attorney-name { position: absolute; left: 590px; top: 333px; width: 280px; text-align: center;
    font-family: "Cinzel", serif; font-size: 29px; line-height: 1.15; color: var(--gold); }
  .cta-panel { position: absolute; left: 584px; top: 407px; width: 286px; height: 433px; background: var(--white); }
  .cta-headline { position: absolute; left: 0; width: 100%; text-align: center; font-family: "Yanone Kaffeesatz", sans-serif; color: var(--red); font-weight: 400; }
  .cta-injured { top: 18px; font-size: 66px; }
  .cta-help { top: 110px; font-size: 50px; }
  .cta-rule { position: absolute; left: 16px; top: 212px; width: 254px; height: 3px; background: #222; }
  .cta-call { position: absolute; left: 22px; top: 242px; display: flex; align-items: center; gap: 12px;
    font-family: "Cinzel", serif; font-size: 24px; color: #111; }
  .call-icon { width: 26px; height: 26px; background: linear-gradient(180deg, #e7b64c, #9c6a1c); display: flex; align-items: center; justify-content: center; }
  .consult-button { position: absolute; left: 13px; top: 297px; width: 261px; height: 112px; border-radius: 10px;
    background: linear-gradient(180deg, #e8847a 0%, var(--red-bright) 40%, var(--red) 100%);
    border: 2px solid #a32d2a; text-align: center; color: var(--white); font-family: "Yanone Kaffeesatz", sans-serif; }
  .consult-free { font-size: 54px; line-height: 1; margin-top: 6px; }
  .consult-label { font-size: 40px; line-height: 1; }
  .phone-label { position: absolute; left: 73px; top: 664px; font-family: "Cinzel", serif; font-size: 27px; letter-spacing: 1px; color: var(--white); }
  .phone-number { position: absolute; left: 71px; top: 700px; font-family: "Arimo", Arial, sans-serif; font-weight: 700; font-size: 52px; color: var(--gold); }
  .values { position: absolute; left: 50px; top: 808px; list-style: none; }
  .values li { display: flex; align-items: center; height: 58px; font-family: "Cinzel", serif; font-size: 32px; color: var(--gold); }
  .values li:nth-child(3) { height: 62px; }
  .values svg { margin-right: 14px; }
  .divider-vertical { position: absolute; left: 304px; top: 840px; width: 1px; height: 148px; background: #888; }
  .services { position: absolute; left: 328px; top: 843px; width: 550px; }
  .services-title { font-size: 25px; font-weight: 400; color: var(--white); margin-bottom: 6px; }
  .services-list { font-size: 15px; line-height: 19px; color: var(--amber); }
  .services-list span { color: var(--white); }
  .rule-services { position: absolute; left: 309px; top: 994px; width: 566px; height: 1px; background: #bbb; }
  .website { position: absolute; left: 330px; top: 1003px; font-weight: 700; font-size: 43px; color: var(--gold); }
  .rule-footer { position: absolute; left: 60px; top: 1063px; width: 814px; height: 1px; background: #bbb; }
  .footer-address, .footer-contacts { position: absolute; top: 1102px; font-size: 14px; line-height: 19px; color: var(--white); }
  .footer-address { left: 71px; }
  .footer-contacts { left: 289px; display: grid; grid-template-columns: 78px auto; }
  .follow-box { position: absolute; left: 611px; top: 1094px; width: 252px; height: 93px; background: var(--footer-box); }
  .follow-label { position: absolute; left: 30px; top: 4px; font-size: 12px; font-weight: 700; color: var(--white); }
  .social-row { position: absolute; left: 28px; top: 30px; display: flex; gap: 12px; }
  .social-chip { width: 42px; height: 42px; border-radius: 8px; background: #6f7782; }
</style>
</head>
<body>
<main class="flyer">
  <svg class="backdrop" width="927" height="1200" viewBox="0 0 927 1200" aria-hidden="true">
    <defs>
      <linearGradient id="steelBand" x1="0" y1="0" x2="1" y2="1">
        <stop offset="0" stop-color="#22344a"/>
        <stop offset="0.6" stop-color="var(--steel)"/>
        <stop offset="1" stop-color="#0c1118"/>
      </linearGradient>
      <linearGradient id="goldBand" x1="0" y1="0" x2="1" y2="0">
        <stop offset="0" stop-color="#b37a22"/>
        <stop offset="0.5" stop-color="#e2b04c"/>
        <stop offset="1" stop-color="#f0c868"/>
      </linearGradient>
    </defs>
    <path d="M0 0 H927 V300 C860 180 760 90 560 70 C380 55 200 90 0 160 Z" fill="url(#steelBand)"/>
    <path d="M0 590 C200 560 420 560 620 600 C720 620 820 640 927 630 V660 C780 680 640 650 470 640 C300 630 150 650 0 690 Z" fill="url(#goldBand)"/>
  </svg>

  <div class="crash-photo" role="img" aria-label="Photo of a damaged silver car beside a red fire truck at an accident scene"></div>

  <div class="logo-plate"><p class="logo-name">Brightwell Law Group</p></div>

  <div class="attorney-portrait" role="img" aria-label="Portrait photo of attorney Morgan Ellis Brightwell in a dark suit"></div>
  <h2 class="attorney-name">Morgan Ellis<br>Brightwell</h2>

  <section class="cta-panel">
    <p class="cta-headline cta-injured">INJURED?</p>
    <p class="cta-headline cta-help">WE CAN HELP.</p>
    <div class="cta-rule"></div>
    <p class="cta-call">
      <span class="call-icon"><svg width="12" height="14" viewBox="0 0 12 14"><path d="M9 2 L3 7 L9 12" fill="none" stroke="#111" stroke-width="1.6"/></svg></span>
      Call us today
    </p>
    <div class="consult-button">
      <p class="consult-free">FREE</p>
      <p class="consult-label">CONSULTATION</p>
    </div>
  </section>

  <p class="phone-label">PHONE NUMBER:</p>
  <p class="phone-number">1-855-MBRIGHT</p>

  <ul class="values">
    <li><svg width="24" height="24" viewBox="0 0 24 24"><path d="M3 13 L9 20 L21 3" fill="none" stroke="#fff" stroke-width="3"/></svg>Passion</li>
    <li><svg width="24" height="24" viewBox="0 0 24 24"><path d="M3 13 L9 20 L21 3" fill="none" stroke="#fff" stroke-width="3"/></svg>Success</li>
    <li><svg width="24" height="24" viewBox="0 0 24 24"><path d="M3 13 L9 20 L21 3" fill="none" stroke="#fff" stroke-width="3"/></svg>Knowledge</li>
    <li><svg width="24" height="24" viewBox="0 0 24 24"><path d="M3 13 L9 20 L21 3" fill="none" stroke="#fff" stroke-width="3"/></svg>Tenacity</li>
  </ul>

  <div class="divider-vertical"></div>
  <section class="services">
    <h3 class="services-title">Our Services:</h3>
    <p class="services-list">Car accidents, big truck accidents, DUI injury accidents, motorcycle accident, pedestrian accident injury, passenger accident injury, worker's compensation, medical malpractice, nursing home abuse, dog bite injury, hospital injury, dental injury, pharmaceutical injury <span>and</span> premise injury, <span>as well as several other injury claims.</span></p>
  </section>

  <div class="rule-services"></div>
  <p class="website">www.brightwelllawfirm.com</p>
  <div class="rule-footer"></div>

  <address class="footer-address" style="font-style:normal">
    Brightwell Law Group<br>412 Harbor Row<br>Savannah, GA 31405
  </address>
  <div class="footer-contacts">
    <span>Savannah</span><span>: (912) 555-0142</span>
    <span>Toll Free</span><span>: (855) MBRIGHT</span>
    <span>Fax</span><span>: (912) 555-0147</span>
  </div>

  <aside class="follow-box">
    <p class="follow-label">Follw us</p>
    <div class="social-row">
      <span class="social-chip"></span>
      <span class="social-chip"></span>
      <span class="social-chip"></span>
      <span class="social-chip"></span>
    </div>
  </aside>
</main>
</body>
</html>
```